Brindle Structures Construction Company Seeking Modern Website

We are a small construction company wanting to create a web presence. We don't have much in the way of current content but will get photos as they come in. Attached is a picture of our business card.
The pages we would like on the menu are:
Home
Portfolio
Product Specs
Testimonials
Our Process
Contact
Some designs we like are:
http://www.tovenquarnsheds.example/
http://www.qzrsheds.example/
http://pannowsheds.example/
http://wistenhalls.example/
Not much requirements other than that so feel free to be creative!
Updates
Target Market(s)
Construction
Commercial and Residential Buildings
Industry/Entity Type
Construction Company
Number of Pages Required
5+ page
Look and feel

```html
<!DOCTYPE html>
<html lang="en">
<head>
<meta charset="utf-8">
<title>Brindle Structures Construction Company</title>
<link rel="stylesheet" href="https://fonts.googleapis.com/css2?family=Open+Sans:wght@400;600;700;800&display=swap">
<style>
:root{
  --navy:#2b2452;
  --yellow:#f3c04b;
  --gold:#a37b2c;
  --ink:#141414;
  --grey:#6c6c6c;
  --white:#ffffff;
  --footer:#0a0a0a;
}
*{box-sizing:border-box;margin:0;padding:0}
html,body{width:1200px;height:5187px;overflow:hidden}
body{position:relative;background:var(--white);font-family:"Open Sans",Arial,sans-serif;color:var(--ink)}
.abs{position:absolute}

/* header */
.site-header{left:0;top:0;width:1200px;height:156px;background:var(--navy)}
.brand{left:97px;top:76px;font-size:22px;font-weight:700;color:var(--yellow);white-space:nowrap}
.main-nav{left:321px;top:80px;display:flex;gap:28px}
.main-nav a{color:var(--white);font-size:15px;font-weight:700;text-decoration:none;letter-spacing:.3px}

/* hero */
.hero-photo{left:0;top:156px;width:1200px;height:715px;background:linear-gradient(180deg,#5f87b4 0%,#9fb7cd 30%,#b58a3c 60%,#6e5232 100%)}
.hero-shade{left:0;top:156px;width:1200px;height:715px;background:rgba(0,0,0,.18)}
.hero-title{left:0;top:548px;width:1200px;text-align:center;color:var(--white);font-size:62px;font-weight:400;letter-spacing:26px}
.hero-sub{left:0;top:628px;width:1200px;text-align:center;color:var(--white);font-size:26px;font-weight:700;letter-spacing:2px}
.hero-btn{left:495px;top:722px;width:210px;height:44px;border:2px solid var(--white);color:var(--white);font-size:15px;font-weight:600;letter-spacing:2px;text-align:center;line-height:40px}
.hero-arrow{top:430px}

/* quote bar */
.quote-bar{left:0;top:871px;width:1200px;height:87px}
.quote-text{left:104px;top:900px;color:var(--white);font-size:19px;font-weight:700}
.quote-cta{left:880px;top:899px;color:var(--white);font-size:19px;font-weight:700;letter-spacing:1px}

/* intro cards */
.card-photo{top:1003px;width:318px;height:207px;background:linear-gradient(160deg,#7fa6cf,#a7b3bb 55%,#c89a4b)}
.card-title{top:1216px;font-size:17px;font-weight:700;width:330px}
.card-text{top:1252px;width:318px;font-size:15.5px;line-height:22px;color:#333}
.card-btn{top:1392px;height:40px;padding:0 10px;border:2.5px solid var(--ink);font-size:15px;font-weight:700;line-height:35px}

/* section bands */
.band{left:0;width:1200px;height:87px}
.band-shadow{left:0;width:1200px;height:14px;background:linear-gradient(180deg,#ffffff,#cfcfcf)}
.band-title{left:0;width:1200px;text-align:center;color:var(--white);font-size:44px;font-weight:700;letter-spacing:3px}

/* projects */
.filter{top:1602px;height:34px;padding:0 8px;border:2px solid var(--yellow);color:var(--gold);font-size:15px;line-height:30px;letter-spacing:.5px}
.filter.is-active{background:var(--yellow);color:var(--ink)}
.project-photo{width:390px;height:325px}

/* specs */
.spec-side{top:2496px;width:150px;height:420px;background:linear-gradient(90deg,#f4f4f4,#d8d8d8,#f4f4f4)}
.spec-head{font-size:30px;font-weight:800;color:var(--yellow);line-height:32px}
.spec-text{font-size:16px;line-height:21px;color:#222}
.spec-left{text-align:right;width:385px;left:103px}
.spec-right{width:400px;left:684px}
.spec-icon{width:76px;height:70px}

/* testimonial */
.testimonial-bg{left:0;top:3070px;width:1200px;height:663px;background:linear-gradient(180deg,#c9c9cc 0%,#9a9aa0 45%,#6e6e74 100%)}
.what-say{left:0;top:3083px;width:1200px;text-align:center;font-size:28px;font-weight:600;color:var(--ink)}
.client-name{left:0;top:3423px;width:1200px;text-align:center;font-size:30px;color:var(--ink)}
.quote-body{left:130px;top:3545px;width:940px;text-align:center;font-size:17px;line-height:22px;color:var(--white)}

/* skills */
.skills-text{left:110px;top:3848px;width:980px;text-align:center;font-size:16.5px;line-height:22px;color:#222}
.skill-bar{height:58px;border-radius:14px;background:var(--ink);overflow:hidden;width:490px}
.skill-fill{height:100%;background:var(--yellow);border-radius:14px}
.skill-label{font-size:17px;font-weight:700;color:var(--ink)}

/* stats */
.stats-bg{left:0;top:4235px;width:1200px;height:473px;background:linear-gradient(180deg,#8d9bb8,#7b82a2 50%,#5d6684)}
.stats-title{left:0;top:4250px;width:1200px;text-align:center;color:var(--white);font-size:44px;font-weight:700;line-height:44px;letter-spacing:1.5px}
.stat-num{top:4511px;width:240px;text-align:center;color:var(--white);font-size:38px;font-weight:700}
.stat-label{top:4561px;width:240px;text-align:center;color:var(--white);font-size:17px}

/* footer */
.site-footer{left:0;top:4791px;width:1200px;height:396px;background:var(--footer)}
.foot-head{top:4883px;color:var(--white);font-size:27px;font-weight:700;letter-spacing:1.5px}
.foot-text{color:var(--white);font-size:16.5px;line-height:26px}
.contact-line{display:flex;gap:12px;align-items:flex-start}
.social{top:4948px;width:30px;height:30px;background:var(--yellow)}
</style>
</head>
<body>

<header class="abs site-header"></header>
<div class="abs brand">Brindle Structures</div>
<nav class="abs main-nav">
  <a href="#">HOME</a><a href="#">PORTFOLIO</a><a href="#">PRODUCT SPECS</a><a href="#">TESTIMONIALS</a><a href="#">OUR PROCESS</a><a href="#">CONTACT</a>
</nav>

<div class="abs hero-photo" role="img" aria-label="Yellow excavator digging on a construction site under a blue sky"></div>
<div class="abs hero-shade"></div>
<svg class="abs hero-arrow" style="left:96px" width="36" height="54" viewBox="0 0 36 54"><polyline points="30,4 8,27 30,50" fill="none" stroke="#fff" stroke-width="7"/></svg>
<svg class="abs hero-arrow" style="left:1068px" width="36" height="54" viewBox="0 0 36 54"><polyline points="6,4 28,27 6,50" fill="none" stroke="#fff" stroke-width="7"/></svg>
<h1 class="abs hero-title">WELCOME</h1>
<p class="abs hero-sub">CREATING A BRIGTER FUTURE, TOGETHER</p>
<div class="abs hero-btn">CONTACT US</div>

<svg class="abs quote-bar" viewBox="0 0 1200 87" preserveAspectRatio="none"><rect width="1200" height="87" fill="#f3c04b"/><polygon points="800,0 1200,0 1200,87 760,87" fill="#a37b2c"/></svg>
<p class="abs quote-text">If you find a high quality constructor for your project?</p>
<p class="abs quote-cta">GET A QUOTE &gt;&gt;</p>

<div class="abs card-photo" style="left:110px" role="img" aria-label="Engineers in hard hats on a building site"></div>
<div class="abs card-photo" style="left:446px;background:linear-gradient(170deg,#7a9fc8,#b9c7d4 60%,#d4a85a)" role="img" aria-label="Glass and steel facade of a tower"></div>
<div class="abs card-photo" style="left:774px;background:linear-gradient(160deg,#b98b3c,#d6c9a6 50%,#8aa8c6)" role="img" aria-label="Workers in safety vests at a steel frame site"></div>
<h3 class="abs card-title" style="left:110px">About Brindle Ltd.,</h3>
<h3 class="abs card-title" style="left:446px">Best Facade Renovation</h3>
<h3 class="abs card-title" style="left:774px">Why Choose Us?</h3>
<p class="abs card-text" style="left:110px">We are here to help you from the initial phase to the final construction phase. Our mission is to provide you the highest quality work that meets your expectation</p>
<p class="abs card-text" style="left:446px">We are here to help you from the initial phase to the final construction phase. Our mission is to provide you the highest quality work that meets your expectation</p>
<p class="abs card-text" style="left:774px">We are here to help you from the initial phase to the final construction phase. Our mission is to provide you the highest quality work that meets your expectation</p>
<div class="abs card-btn" style="left:110px">READ MORE</div>
<div class="abs card-btn" style="left:446px">READ MORE</div>
<div class="abs card-btn" style="left:774px">READ MORE</div>

<!-- latest projects -->
<div class="abs band-shadow" style="top:1473px"></div>
<svg class="abs band" style="top:1487px" viewBox="0 0 1200 87" preserveAspectRatio="none"><rect width="1200" height="87" fill="#f3c04b"/><polygon points="340,0 830,0 830,87 262,87" fill="#a37b2c"/></svg>
<h2 class="abs band-title" style="top:1500px">LATEST PROJECTS</h2>
<div class="abs filter is-active" style="left:308px">ALL PROJECTS</div>
<div class="abs filter" style="left:491px">OFFICES</div>
<div class="abs filter" style="left:608px">PLAZAS</div>
<div class="abs filter" style="left:729px">RECIDENCES</div>

<div class="abs project-photo" style="left:10px;top:1673px;background:linear-gradient(170deg,#d9d5cf,#7a5b43 55%,#4c5a3a)" role="img" aria-label="Modern house with timber and dark panels"></div>
<div class="abs project-photo" style="left:408px;top:1673px;background:linear-gradient(180deg,#6f9fd6,#e8e4da 55%,#5f8a4a)" role="img" aria-label="Two-storey white villa with garden"></div>
<div class="abs project-photo" style="left:806px;top:1673px;background:linear-gradient(180deg,#2f6fb8,#d8d0c0 50%,#e7dfcf)" role="img" aria-label="Plaza with angled concrete canopy"></div>
<div class="abs project-photo" style="left:10px;top:2005px;background:linear-gradient(160deg,#e6e6e6,#f0f0f0 50%,#e0c53a)" role="img" aria-label="White apartment block with yellow balconies"></div>
<div class="abs project-photo" style="left:408px;top:2005px;background:linear-gradient(180deg,#4b6f9c,#a0703a 50%,#3d9fb6)" role="img" aria-label="Tropical residence with pool at dusk"></div>
<div class="abs project-photo" style="left:806px;top:2005px;background:linear-gradient(180deg,#8fb7e0,#8b7b6b 55%,#4a4640)" role="img" aria-label="Office towers in a city street"></div>

<!-- product specs -->
<div class="abs band-shadow" style="top:2389px"></div>
<svg class="abs band" style="top:2403px" viewBox="0 0 1200 87" preserveAspectRatio="none"><rect width="1200" height="87" fill="#f3c04b"/><polygon points="340,0 830,0 830,87 262,87" fill="#a37b2c"/></svg>
<h2 class="abs band-title" style="top:2416px">PRODUCT SPECS</h2>
<div class="abs spec-side" style="left:0" role="img" aria-label="Pale steel column detail"></div>
<div class="abs spec-side" style="left:1050px" role="img" aria-label="Pale steel column detail"></div>

<div class="abs spec-left" style="top:2535px"><div class="spec-head">STRUCTURE</div><p class="spec-text">Laminated posts a full four feet in the ground, set on an engineered concrete “cookie”</p></div>
<div class="abs spec-right" style="top:2535px"><div class="spec-head">STEEL SLIDING &amp;<br>ROOFING</div><p class="spec-text">29 gauge galvanized steel with a baked on enamel finish</p></div>
<div class="abs spec-left" style="top:2715px"><div class="spec-head">CONCRETE</div><p class="spec-text">4,000 psi concrete with fiber reinforcing Saw cuts every 12’ or closer</p></div>
<div class="abs spec-right" style="top:2715px"><div class="spec-head">FINISHES</div><p class="spec-text">Vapor barrier on the roof<br>Insulated steel service door</p></div>

<svg class="abs spec-icon" style="left:501px;top:2540px" viewBox="0 0 76 70"><rect width="76" height="70" fill="#f3c04b"/><polygon points="18,54 18,32 38,18 58,32 58,54" fill="none" stroke="#141414" stroke-width="5"/><rect x="32" y="38" width="12" height="16" fill="#141414"/></svg>
<svg class="abs spec-icon" style="left:591px;top:2540px" viewBox="0 0 76 70"><rect width="76" height="70" fill="#141414"/><polyline points="12,40 38,18 64,40" fill="none" stroke="#f3c04b" stroke-width="6"/><line x1="18" y1="52" x2="58" y2="52" stroke="#f3c04b" stroke-width="5"/></svg>
<svg class="abs spec-icon" style="left:501px;top:2720px" viewBox="0 0 76 70"><rect width="76" height="70" fill="#141414"/><polygon points="38,14 60,26 38,38 16,26" fill="#f3c04b"/><polygon points="16,30 36,42 36,58 16,46" fill="#f3c04b"/><polygon points="40,42 60,30 60,46 40,58" fill="#f3c04b"/></svg>
<svg class="abs spec-icon" style="left:591px;top:2720px" viewBox="0 0 76 70"><rect width="76" height="70" fill="#141414"/><rect x="24" y="14" width="28" height="18" fill="#f3c04b"/><rect x="34" y="32" width="8" height="24" fill="#f3c04b"/></svg>

<!-- testimonial -->
<div class="abs band-shadow" style="top:2969px"></div>
<svg class="abs band" style="top:2983px" viewBox="0 0 1200 87" preserveAspectRatio="none"><rect width="1200" height="87" fill="#f3c04b"/><polygon points="340,0 830,0 830,87 262,87" fill="#a37b2c"/></svg>
<h2 class="abs band-title" style="top:2996px">TESTIMONIAL</h2>
<div class="abs testimonial-bg" role="img" aria-label="Grey city skyline of high-rise towers"></div>
<p class="abs what-say">What clients say</p>
<svg class="abs" style="left:470px;top:3154px" width="260" height="260" viewBox="0 0 260 260"><circle cx="130" cy="130" r="122" fill="#ffffff"/><circle cx="130" cy="130" r="112" fill="#d9d2c4"/><circle cx="130" cy="130" r="124" fill="none" stroke="#8a8a8a" stroke-width="3"/></svg>
<div class="abs" style="left:488px;top:3172px;width:224px;height:224px;border-radius:50%;background:linear-gradient(180deg,#f0f0f0,#e6b84a 60%,#c9c3b5)" role="img" aria-label="Portrait of the client in a white hard hat"></div>
<p class="abs client-name">Jon Harrow, CEO</p>
<svg class="abs" style="left:568px;top:3482px" width="64" height="36" viewBox="0 0 64 36"><polyline points="4,4 32,32 60,4" fill="none" stroke="#141414" stroke-width="4"/></svg>
<p class="abs quote-body">I am very pleased with the building crew who built our new warehouse and offices. They were honest about costs from the start, kept the site clean and tidy, and finished every stage on schedule. The quality of their work is excellent and every detail was checked with care. We will call on them again for our next project, gladly.</p>

<!-- skills -->
<svg class="abs band" style="top:3740px" viewBox="0 0 1200 87" preserveAspectRatio="none"><rect width="1200" height="87" fill="#f3c04b"/><polygon points="340,0 830,0 830,87 262,87" fill="#a37b2c"/></svg>
<h2 class="abs band-title" style="top:3753px">OUR SKILLS</h2>
<p class="abs skills-text">I am text block. Click edit button to change this text. Lorem ipsum dolor sit amet, consectetur adipiscing elit. Ut elit tellus, luctus nec ullamcorper mattis, pulvinar dapibus leo. Lorem ipsum dolor sit amet, consetetur sadipscing elitr, sed diam nonumy eirmod tempor invidunt ut labore et dolore magna aliquyam erat, sed diam voluptua.t</p>

<div class="abs skill-bar" style="left:104px;top:3975px"><div class="skill-fill" style="width:97%"></div></div><span class="abs skill-label" style="left:132px;top:3992px">Architecture</span>
<div class="abs skill-bar" style="left:606px;top:3975px"><div class="skill-fill" style="width:95%"></div></div><span class="abs skill-label" style="left:634px;top:3992px">House renovation</span>
<div class="abs skill-bar" style="left:104px;top:4048px"><div class="skill-fill" style="width:80%"></div></div><span class="abs skill-label" style="left:132px;top:4065px">Communication</span>
<div class="abs skill-bar" style="left:606px;top:4048px"><div class="skill-fill" style="width:80%"></div></div><span class="abs skill-label" style="left:634px;top:4065px">Professionality</span>
<div class="abs skill-bar" style="left:104px;top:4123px"><div class="skill-fill" style="width:65%"></div></div><span class="abs skill-label" style="left:132px;top:4140px">Innovation</span>
<div class="abs skill-bar" style="left:606px;top:4123px"><div class="skill-fill" style="width:58%"></div></div><span class="abs skill-label" style="left:634px;top:4140px">Low prices</span>

<!-- stats -->
<div class="abs stats-bg" role="img" aria-label="Worker in a hard hat overlooking a building site"></div>
<h2 class="abs stats-title">Leading the way in building<br>and civil construction</h2>
<svg class="abs" style="left:284px;top:4398px" width="110" height="110" viewBox="0 0 110 110"><circle cx="55" cy="55" r="55" fill="#0d0d0d"/><rect x="26" y="44" width="40" height="22" fill="#f3c04b"/><rect x="44" y="32" width="18" height="14" fill="#f3c04b"/><rect x="66" y="54" width="16" height="12" fill="#f3c04b"/><rect x="24" y="70" width="58" height="10" rx="5" fill="#f3c04b"/></svg>
<svg class="abs" style="left:546px;top:4398px" width="110" height="110" viewBox="0 0 110 110"><circle cx="55" cy="55" r="55" fill="#0d0d0d"/><path d="M28 66 Q28 36 55 36 Q82 36 82 66 Z" fill="#f3c04b"/><rect x="22" y="66" width="66" height="8" fill="#f3c04b"/><rect x="51" y="30" width="8" height="16" fill="#0d0d0d"/></svg>
<svg class="abs" style="left:806px;top:4398px" width="110" height="110" viewBox="0 0 110 110"><circle cx="55" cy="55" r="55" fill="#0d0d0d"/><path d="M36 28 H74 V46 Q74 64 55 64 Q36 64 36 46 Z" fill="#f3c04b"/><rect x="51" y="64" width="8" height="12" fill="#f3c04b"/><rect x="40" y="76" width="30" height="8" fill="#f3c04b"/></svg>
<p class="abs stat-num" style="left:219px">2368</p>
<p class="abs stat-num" style="left:481px">999</p>
<p class="abs stat-num" style="left:741px">366</p>
<p class="abs stat-label" style="left:219px">Project Completed</p>
<p class="abs stat-label" style="left:481px">Workers Employed</p>
<p class="abs stat-label" style="left:741px">Awards Won</p>

<!-- contact -->
<svg class="abs band" style="top:4708px;height:83px" viewBox="0 0 1200 83" preserveAspectRatio="none"><rect width="1200" height="83" fill="#f3c04b"/><polygon points="340,0 830,0 830,83 262,83" fill="#a37b2c"/></svg>
<h2 class="abs band-title" style="top:4718px">CONTACT</h2>

<footer class="abs site-footer"></footer>
<h4 class="abs foot-head" style="left:97px">BRINDLE STRUCTURES</h4>
<h4 class="abs foot-head" style="left:519px">OUR CONTACT</h4>
<h4 class="abs foot-head" style="left:926px">FOLLOW US</h4>
<p class="abs foot-text" style="left:97px;top:4952px;width:300px">Lorem ipsum dolor sit amet, onsectetur adipiscing elit. Quisque nec erat erat, er blandit, nulla quis fermentum, orem ipsum dolor sit amet, onsectetur adipiscing elit.</p>
<div class="abs foot-text" style="left:527px;top:4952px">
  <div class="contact-line"><svg width="16" height="22" viewBox="0 0 16 22" style="margin-top:3px"><path d="M8 0 C3 0 0 4 0 8 C0 13 8 22 8 22 C8 22 16 13 16 8 C16 4 13 0 8 0 Z" fill="#fff"/><circle cx="8" cy="8" r="3" fill="#0a0a0a"/></svg><span>Brindle Structures<br>P.O. Box 207,<br>Marrowvale IN 40012</span></div>
  <div class="contact-line" style="margin-top:12px"><svg width="16" height="22" viewBox="0 0 16 22" style="margin-top:3px"><rect x="3" y="1" width="10" height="20" rx="2" fill="#fff"/><rect x="5" y="4" width="6" height="12" fill="#0a0a0a"/></svg><span>1-800-555-0142</span></div>
  <div class="contact-line" style="margin-top:12px"><svg width="16" height="22" viewBox="0 0 16 22" style="margin-top:3px"><rect x="0" y="6" width="16" height="12" fill="#fff"/><polyline points="0,6 8,13 16,6" fill="none" stroke="#0a0a0a" stroke-width="1.5"/></svg><span>info@example.com</span></div>
</div>
<div class="abs social" style="left:946px"></div>
<div class="abs social" style="left:988px"></div>
<div class="abs social" style="left:1030px"></div>

</body>
</html>
```